Summer Music/Chorus/Choir Camp for Young Singers Ages 8-13

We need a flyer for a summer camp for young singers ages 8-13. We are nonprofit community children's chorus in Miami, FL. Our camp provides specialized training in music theory, sight-reading,and aural training through daily choral rehearsals in an environment that is both positive and a lot of fun! Our camp offers children the opportunity to come as they are, no matter the level of experience, and grow tremendously in their musicianship skills. In addition to this, our campers participate in song-writing, masterclasses, community performances, and media projects. The final design should be clean, fun, not too crowded, should appeal to boys and girls ages 8-13, and something someone that age would consider "cool" and not too childish. Drawings are cool, something different.
Updates

Target Market(s)

Ages 8-13 and parents of those kids.

Industry/Entity Type

Community

Requirements
Must have
• All info attached.
Nice to have
• Things that relate to music, especially related to singing/choirs
Should not have
• instruments, stock photos of children, or photos from our website (unless they are used very creatively), or photos in general. I've attached our previous camp flyer and our current organization flyer but I don't necessarily want this flyer to look like those.

```html
<!DOCTYPE html>
<html lang="en">
<head>
<meta charset="utf-8">
<title>Children's Chorus Summer Camp</title>
<link href="https://fonts.googleapis.com/css2?family=Fjalla+One&family=Open+Sans:ital,wght@0,400;0,600;0,700;1,400&display=swap" rel="stylesheet">
<style>
  :root {
    --teal: #1ba3ab;
    --teal-dark: #0d7e87;
    --teal-light: #8fd3d6;
    --navy: #17396b;
    --ink: #3b3b3b;
    --paper: #ffffff;
    --mist: #eef3f4;
  }
  * { margin: 0; padding: 0; box-sizing: border-box; }
  html, body { width: 900px; height: 1200px; overflow: hidden; background: var(--paper); }
  .flyer {
    position: relative; width: 900px; height: 1200px; overflow: hidden;
    background: var(--paper); font-family: "Open Sans", sans-serif; color: var(--ink);
  }
  .brand {
    position: absolute; left: 50px; top: 45px; display: flex; align-items: center; gap: 14px;
    font-family: "Fjalla One", sans-serif; color: var(--teal); font-size: 34px; line-height: 1;
  }
  .brand-dot { width: 22px; height: 22px; border-radius: 50%; background: var(--teal); }
  .notes-art {
    position: absolute; right: 20px; top: 30px; width: 470px; height: 210px;
    background: linear-gradient(120deg, #fde9f0 0%, #e4f4f7 55%, #fff6dc 100%); border-radius: 12px;
  }
  .title {
    position: absolute; left: 60px; top: 200px; font-family: "Fjalla One", sans-serif; font-weight: 400;
    color: var(--navy); font-size: 64px; line-height: 1.02; letter-spacing: 1px;
  }
  .kids-art {
    position: absolute; right: 40px; top: 240px; width: 400px; height: 150px;
    background: linear-gradient(90deg, #ffe7c8, #d7eef7); border-radius: 14px;
  }
  .wave { position: absolute; left: 0; top: 380px; width: 900px; height: 100px; }
  .details { position: absolute; left: 60px; top: 482px; width: 360px; color: var(--teal-dark); }
  .details h2 { font-family: "Fjalla One", sans-serif; font-weight: 400; font-size: 32px; line-height: 1.1; }
  .details p { font-size: 20px; font-weight: 600; line-height: 1.4; margin-bottom: 14px; }
  .details .note { font-size: 17px; font-style: italic; font-weight: 400; margin-bottom: 0; }
  .about {
    position: absolute; left: 450px; top: 470px; width: 430px; height: 230px;
    background: var(--teal); color: var(--paper); padding: 22px 26px;
    font-size: 15.5px; line-height: 1.45; font-style: italic;
  }
  .contact { position: absolute; right: 40px; top: 725px; text-align: right; color: var(--teal-dark); }
  .contact h3 { font-family: "Fjalla One", sans-serif; font-weight: 400; font-size: 30px; }
  .contact-line { display: flex; justify-content: flex-end; align-items: center; gap: 10px; font-size: 22px; font-weight: 700; }
  .contact-line svg { width: 20px; height: 20px; fill: var(--teal-dark); }
  .location { position: absolute; left: 450px; top: 840px; width: 430px; font-size: 16px; line-height: 1.4; }
  .nonprofit {
    position: absolute; left: 450px; top: 920px; width: 430px; padding: 14px 18px;
    background: var(--mist); font-size: 15px; font-style: italic; line-height: 1.4;
  }
  .photo-area {
    position: absolute; left: 0; top: 830px; width: 410px; height: 370px;
    background: linear-gradient(160deg, #f4f7f8 0%, #d9e6ea 60%, #b9ccd3 100%);
  }
  .partners { position: absolute; left: 450px; top: 1060px; width: 430px; display: flex; align-items: center; gap: 24px; }
  .partner-name { font-weight: 700; font-size: 18px; color: var(--ink); display: flex; align-items: center; gap: 8px; }
  .partner-name span { width: 14px; height: 14px; background: var(--ink); display: inline-block; }
  .badge { height: 50px; background: #cfd8db; }
  .badge.wide { width: 110px; }
  .badge.square { width: 60px; }
</style>
</head>
<body>
<main class="flyer">
  <div class="brand"><span class="brand-dot"></span>Bright Harmony Chorus</div>
  <div class="notes-art" role="img" aria-label="Colourful illustration of flowing music staff with notes"></div>
  <h1 class="title">CHILDREN'S<br>CHORUS</h1>
  <div class="kids-art" role="img" aria-label="Cartoon illustration of children singing together"></div>

  <svg class="wave" viewBox="0 0 900 100" preserveAspectRatio="none" aria-hidden="true">
    <path d="M0 40 C250 95 600 -10 900 45 L900 100 L0 100 Z" fill="var(--teal-light)"/>
    <path d="M0 60 C260 110 620 10 900 65 L900 100 L0 100 Z" fill="var(--teal)"/>
    <path d="M0 90 C300 100 600 80 900 90 L900 100 L0 100 Z" fill="var(--paper)"/>
  </svg>

  <section class="details">
    <h2>Dates and Times</h2>
    <p>July 18-29, 9am-3pm (M-F)*</p>
    <h2>Extended hours<br>available</h2>
    <p>(7:30am-5:30pm)<br>for an extra $50 per week.</p>
    <h2>Cost- *$300<br>for 2-week session</h2>
    <p class="note">*Price does not include lunch</p>
  </section>

  <section class="about">
    "Youth and children who love to sing will have a blast at our choral camp! Our music educators and industry professionals are dedicated to enhancing the lives of young singers through choral training which develops vocal technique, ear training, music reading, and interpersonal skills. Activities are fun and interactive and former music training is not necessary. Singers in grades 3-9 are invited to attend! Register today!"
  </section>

  <section class="contact">
    <h3>Contact Us</h3>
    <div class="contact-line"><svg viewBox="0 0 24 24"><path d="M6.6 10.8a15 15 0 0 0 6.6 6.6l2.2-2.2c.3-.3.7-.4 1-.2 1.1.4 2.3.6 3.6.6.6 0 1 .4 1 1V20c0 .6-.4 1-1 1A17 17 0 0 1 3 4c0-.6.4-1 1-1h3.5c.6 0 1 .4 1 1 0 1.3.2 2.5.6 3.6.1.3 0 .7-.2 1z"/></svg>305.555.0148</div>
    <div class="contact-line"><svg viewBox="0 0 24 24"><path d="M2 5h20v14H2z M2 5l10 8 10-8" fill="none" stroke="var(--teal-dark)" stroke-width="2"/></svg>hello@brightharmonychorus.org</div>
  </section>

  <p class="location">Location- Palmetto Bay Arts Hall,<br>4820 SW 180th Street Miami, FL 33157</p>
  <p class="nonprofit">"Bright Harmony is a 501 (c)3 Nonprofit organization. Donations made to BHC are tax-exempt."</p>

  <div class="photo-area" role="img" aria-label="Photo area: young musician performing"></div>

  <div class="partners">
    <div class="partner-name"><span></span>Lumen Trust</div>
    <div class="badge wide"></div>
    <div class="badge square"></div>
  </div>
</main>
</body>
</html>
```